brindle's business card for earthmoving and tipper hire business.

I have a small earthmoving and tipper truck company. I am aiming for the smaller jobs that the big guys don't want. I am also Doing grass slashing and fire hazard reduction work. I would like to see some earthy colors, greens browns etc. I have a tractor with a front end loader attachment, and a 22 ton tipper. I would like to maybe have a silhouette of a tipper and tractor/slasher/loader setup in centre with my business name over the top and details to one side or something like that

Industry/Entity Type

Business

Contact Information for Business Card

Brindle's small earthworks and tipper hireToowoombaABN: 47781050480PH 0479126773Email brindle.4@fenwickmail.com

Font styles to use
Sans Serif

Colors
fbee3d
abd036
85cae6
f78f20

Requirements
Nice to have
• Earthy colors . business name in blue

```html
<!DOCTYPE html>
<html lang="en">
<head>
<meta charset="utf-8">
<title>Brindle's Earthworks and Tipper – Business Card</title>
<link rel="stylesheet" href="https://fonts.googleapis.com/css2?family=Oswald:wght@700&family=Open+Sans:wght@400;600&display=swap">
<style>
  :root {
    --paper: #e6e2d4;
    --hill: #67625d;
    --brand: #c4552e;
    --vehicles: #6f6b66;
    --arc-text: #e2ded6;
    --service: #f1ec3c;
    --bullet: #a6d23a;
    --details: #d8d4cc;
  }
  html, body {
    margin: 0;
    padding: 0;
    overflow: hidden;
    background: #ffffff;
  }
  .card {
    position: relative;
    width: 1200px;
    height: 741px;
    background: var(--paper);
    overflow: hidden;
    font-family: "Open Sans", Arial, sans-serif;
  }
  .card__art {
    position: absolute;
    inset: 0;
  }
  .brand-name {
    position: absolute;
    top: 88px;
    left: 0;
    width: 100%;
    margin: 0;
    text-align: center;
    font-family: "Oswald", "Arial Narrow", sans-serif;
    font-weight: 700;
    font-size: 82px;
    line-height: 1;
    letter-spacing: 2px;
    color: var(--brand);
  }
  .arc-title {
    font-family: "Open Sans", Arial, sans-serif;
    font-size: 33px;
    letter-spacing: 0.5px;
    fill: var(--arc-text);
  }
  .services {
    position: absolute;
    top: 510px;
    left: 0;
    width: 100%;
    margin: 0;
    padding: 0;
    list-style: none;
    text-align: center;
    color: var(--service);
    font-size: 30px;
    line-height: 44px;
  }
  .services__row { display: block; }
  .service { display: inline-block; margin: 0 10px; }
  .service::before {
    content: "";
    display: inline-block;
    width: 11px;
    height: 11px;
    margin-right: 10px;
    border-radius: 50%;
    background: var(--bullet);
    vertical-align: middle;
    position: relative;
    top: -3px;
  }
  .details {
    position: absolute;
    top: 630px;
    left: 0;
    width: 100%;
    margin: 0;
    text-align: center;
    color: var(--details);
    font-size: 25px;
    letter-spacing: 0.3px;
  }
  .details__sep { margin: 0 22px; }
</style>
</head>
<body>
<main class="card">
  <svg class="card__art" width="1200" height="741" viewBox="0 0 1200 741" aria-hidden="false">
    <rect class="vehicles" x="385" y="255" width="395" height="118" rx="10" fill="var(--vehicles)" role="img" aria-label="Silhouettes of a tipper truck and a tractor with front-end loader"/>
    <path class="hill" d="M0 428 C 300 340, 700 330, 1200 452 L1200 741 L0 741 Z" fill="var(--hill)"/>
    <path id="arc-line" d="M95 462 Q 600 372 1105 458" fill="none"/>
    <text class="arc-title">
      <textPath href="#arc-line" startOffset="50%" text-anchor="middle">Brindle's Small Earthworks &amp; Tipper Hire, Toowoomba</textPath>
    </text>
  </svg>

  <h1 class="brand-name">BRINDLE'S</h1>

  <ul class="services">
    <li class="services__row">
      <span class="service">Small Earthworks</span>
      <span class="service">Slashing</span>
      <span class="service">Fire Hazard Reduction</span>
    </li>
    <li class="services__row">
      <span class="service">Rural Cleanups</span>
      <span class="service">Tipper</span>
    </li>
  </ul>

  <p class="details">
    <span>ABN: 62194038715</span><span class="details__sep">|</span><span>PH 0438571629</span><span class="details__sep">|</span><span>Email brindle.4@fenwickmail.com</span>
  </p>
</main>
</body>
</html>
```